Coming Soon page for a new fitness startup

We are a new startup based in Toronto, Canada working on a site and mobile app where people can register for athletic events such as running, cycling, triathlon, SUP, etc.

Participants will also be able to manage their clubs and team, and connect their fitness trackers so they have all their fitness data and friends in one place.

I like very simple designs and lots of whitespace. So no need for icons or unnecessary graphics.

I prefer having a mobile phone app instead of a hero image. No need to worry about the details within the mobile app for now, we can fill it in later. Here are some landing pages that I like.
https://pixelshelf.example/tormundlaksa/buckets/493817-Landing-Page

Attached is a wireframe that gives some sample content for each of the sections. Please do not take the wireframe too literally, it is only meant to illustrate the content that we are experimenting with and should give an idea of how much text will be on the page.

I have also attached the company logo files. The logo is not being used yet so feel free to simplify the logo if it doesn't look great with your design. For example, I'm ok with just the name "vexqari" in white if that looks better.

Target Market(s)

Ages 25 to 45. Interested in running, cycling, triathlon, SUP, etc.

Industry/Entity Type

Fitness

Coding

Coded - Design and coding required

Number of Pages Required

1 page

Requirements
Should not have
• Any photos should not contain track and field events, or people in a gym. Any photos should have people running or cycling outdoors. I know that photos can be easily swapped out but it is distracting to review a design that has the wrong photos.

```html
<!DOCTYPE html>
<html lang="en">
<head>
<meta charset="utf-8">
<title>vexqari — Launching Spring 2018</title>
<link href="https://fonts.googleapis.com/css2?family=Rubik:wght@400;500&family=Raleway:wght@300;400&family=Roboto:wght@300;400;500&display=swap" rel="stylesheet">
<style>
  :root{
    --red:#d0202f;
    --ink:#58585a;
    --body:#555557;
    --hero-bg:#f3f3f3;
    --band-bg:#f5f5f5;
    --panel:#464648;
    --white:#ffffff;
    --line:#e2e2e2;
  }
  *{box-sizing:border-box;margin:0;padding:0}
  html,body{width:913px;height:1200px;overflow:hidden}
  body{position:relative;background:var(--white);font-family:'Roboto',sans-serif;color:var(--body)}
  .abs{position:absolute}
  .red{color:var(--red)}

  /* hero */
  .hero{left:0;top:0;width:913px;height:509px;background:linear-gradient(135deg,#f7f7f7,#eeeeee)}
  .brand{left:65px;top:10px;display:flex;align-items:center;gap:6px;font-family:'Rubik',sans-serif;font-size:26px;font-weight:400;color:var(--ink)}
  .brand-dot{width:20px;height:20px;border-radius:50%;background:var(--red)}
  .launch{right:66px;top:24px;font-family:'Rubik',sans-serif;font-size:21px;color:var(--ink);letter-spacing:-.3px}
  .launch span{color:var(--red)}
  .device-art{left:22px;top:84px;width:324px;height:425px;border-radius:60px 60px 0 0;background:linear-gradient(180deg,#f1ddd6 0%,#e9c8bd 100%)}
  .device-art::after{content:"";position:absolute;left:120px;top:2px;width:160px;height:340px;border-radius:22px;background:linear-gradient(180deg,#fafafa,#e8e8e8);box-shadow:inset 0 0 0 10px #ffffff}
  .hero-title{left:370px;top:146px;font-family:'Rubik',sans-serif;font-weight:500;font-size:32px;line-height:40px;color:var(--ink);letter-spacing:-.2px}
  .hero-copy{left:370px;top:238px;width:450px;font-size:12.8px;line-height:16px;color:var(--body)}
  .hero-note{left:370px;top:290px;width:350px;font-size:12.8px;line-height:16px;color:var(--red)}
  .notify{left:369px;top:332px;display:flex;gap:9px}
  .field{background:var(--white);border:1px solid var(--line);font-family:'Roboto',sans-serif;font-size:10px;color:#666;display:flex;align-items:center;padding-left:10px}
  .notify .field{width:332px;height:40px}
  .btn{background:var(--red);color:var(--white);font-family:'Roboto',sans-serif;font-weight:500;font-size:12.5px;display:flex;align-items:center;justify-content:center}
  .notify .btn{width:124px;height:41px}

  /* features */
  .features-title{left:0;width:913px;top:544px;text-align:center;font-family:'Rubik',sans-serif;font-weight:500;font-size:38px;color:var(--ink);letter-spacing:-.3px}
  .features-sub{left:0;width:913px;top:590px;text-align:center;font-family:'Raleway',sans-serif;font-weight:400;font-size:19px;color:var(--ink)}
  .feature{top:650px;width:230px}
  .feature h3{font-family:'Rubik',sans-serif;font-weight:500;font-size:15px;color:var(--ink);margin-bottom:12px}
  .feature p{font-size:11.4px;line-height:16px;font-weight:300;color:var(--body)}
  .divider{top:636px;width:1px;height:118px;background:var(--line)}

  /* organizer */
  .organizer{left:0;top:784px;width:913px;height:373px;background:var(--band-bg)}
  .org-title{left:65px;top:860px;font-family:'Rubik',sans-serif;font-weight:500;font-size:27px;color:var(--ink)}
  .org-sub{left:65px;top:898px;font-family:'Raleway',sans-serif;font-size:18px;color:var(--ink)}
  .org-copy{left:65px;top:933px;width:340px;font-size:12.8px;line-height:17.5px;color:var(--body)}
  .org-link{left:65px;top:1022px;font-family:'Rubik',sans-serif;font-size:12.5px;color:var(--red)}
  .contact{left:437px;top:825px;width:410px;height:302px;background:var(--panel)}
  .contact h2{position:absolute;left:15px;top:18px;font-family:'Rubik',sans-serif;font-weight:500;font-size:25px;color:var(--white);letter-spacing:-.2px}
  .contact .field{position:absolute;left:15px;width:374px;height:45px;border-radius:2px;border:none;font-size:11px;color:#777}
  .contact .btn{position:absolute;left:264px;top:250px;width:125px;height:40px}

  /* footer */
  .site-footer{left:0;top:1157px;width:913px;height:43px;background:var(--red);color:var(--white);font-size:10px;font-weight:500}
  .foot-links{position:absolute;left:65px;top:14px}
  .social{position:absolute;left:424px;top:13px;display:flex;gap:14px}
  .social span{width:13px;height:13px;border-radius:50%;background:var(--white)}
  .copyright{position:absolute;right:66px;top:14px}
</style>
</head>
<body>
  <header>
    <div class="abs hero"></div>
    <div class="abs brand"><span class="brand-dot"></span>vexqari</div>
    <div class="abs launch">Launching <span>Spring 2018</span></div>
  </header>

  <section>
    <div class="abs device-art" role="img" aria-label="Hand holding a smartphone showing the app home screen"></div>
    <h1 class="abs hero-title"><span class="red">Connect Your Training,</span> Friends,<br>and Events in One Place</h1>
    <p class="abs hero-copy">Lorem ipsum dolor sit amet, consectetuer adipiscing elit, sed diam nonum-my nibh euismod tincidunt ut laoreet dolore magna aliquam erat volutpat.</p>
    <p class="abs hero-note">Join our email list. A referral program is coming and you'll want to be the first to know.</p>
    <form class="abs notify">
      <div class="field">Enter Email Address</div>
      <div class="btn">Notify Me</div>
    </form>
  </section>

  <section>
    <h2 class="abs features-title">Training and Racing <span class="red">all in one place</span></h2>
    <p class="abs features-sub">A new fitness community is coming soon.</p>
    <div class="abs feature" style="left:65px"><h3>Find <span class="red">Events</span></h3><p>Lorem ipsum dolor sit amet, consectetuer adipiscing elit, sed diam nonummy nibh euismod tincidunt ut laoreet dolore magna aliquam erat volutpat.</p></div>
    <div class="abs divider" style="left:310px"></div>
    <div class="abs feature" style="left:352px"><h3>Invite <span class="red">Your Friends</span></h3><p>Lorem ipsum dolor sit amet, consectetuer adipiscing elit, sed diam nonummy nibh euismod tincidunt ut laoreet dolore magna aliquam erat volutpat.</p></div>
    <div class="abs divider" style="left:597px"></div>
    <div class="abs feature" style="left:633px"><h3>Connect <span class="red">Your Workouts</span></h3><p>Lorem ipsum dolor sit amet, consectetuer adipiscing elit, sed diam nonummy nibh euismod tincidunt ut laoreet dolore magna aliquam erat volutpat.</p></div>
  </section>

  <section>
    <div class="abs organizer"></div>
    <h2 class="abs org-title">Organizing <span class="red">an Event?</span></h2>
    <p class="abs org-sub">Attracting participants is hard</p>
    <p class="abs org-copy">with your event listed on vexqari we'll not only handle the registration and payment process, we've also made it our own personal mission to drive up participation numbers across all events.</p>
    <a class="abs org-link">Contact us to learn more</a>
    <form class="abs contact">
      <h2>We'd love to hear from you</h2>
      <div class="field" style="top:71px">Your Name</div>
      <div class="field" style="top:129px">Email Address</div>
      <div class="field" style="top:187px">How can we help?</div>
      <div class="btn">Send Now</div>
    </form>
  </section>

  <footer class="abs site-footer">
    <div class="foot-links">About Us &nbsp;|&nbsp; Developers &nbsp;|&nbsp; Careers</div>
    <div class="social" aria-label="Social links"><span></span><span></span><span></span></div>
    <div class="copyright">© 2018 Vexqari Inc.</div>
  </footer>
</body>
</html>
```